Business card design needed

Our company background is that we provides transfers to and from the airport, social & corporate events, weddings.
We are also available for charter for birthday party, wine tastings, concerts, anniversary, school balls etc.
Our business cards have to reflect that we have a professional company, they are our first contact and have to stand out from the other 'players' in the market.

Industry/Entity Type

School

Contact Information for Business Card

VESTAR PTH, Teodor & Marguerite, mob: 0427 381 592, PO Box 284, Brelmont WA 6172, ABN 52 614 203 178, Lic 7169/2058,

Requirements
Must have
• Telephone number: 0427 381 592
Website: www.VESTARPTH.com.au
postal address: PO Box 284, Brelmont WA 6172
Licences: Lic 7169/2058

***If using the new photo (one with the bus and buildings behind it), if possible can the buildings be cropped out. Thanks
Nice to have
• would be nice to have the pics of the vehicle(s), preferred the Vel on the card but not too fussed.
Should not have
• Picture of vehicle we don't have in our fleet. (We ONLY have the Velarions and Murako Densa mini bus)

```html
<!DOCTYPE html>
<html lang="en">
<head>
<meta charset="utf-8">
<title>VESTAR PTH — Business Cards</title>
<link rel="stylesheet" href="https://fonts.googleapis.com/css2?family=Crimson+Text:wght@600;700&display=swap">
<style>
  :root {
    --page-bg: #ececec;
    --card-white: #f4f5f6;
    --card-white-edge: #e2e4e7;
    --blue-deep: #3c55a9;
    --blue-mid: #1f63b8;
    --blue-bright: #0a8ad0;
    --ink-blue: #2f4aa0;
    --ink-cyan: #0d87c8;
    --ink-white: #ffffff;
    --vehicle-light: rgba(60, 85, 169, 0.10);
    --vehicle-dark: rgba(255, 255, 255, 0.10);
  }
  * { box-sizing: border-box; margin: 0; padding: 0; }
  html, body {
    width: 1200px; height: 1004px; overflow: hidden;
    background: var(--page-bg);
    font-family: "Crimson Text", Georgia, serif;
  }
  .card {
    position: absolute;
    width: 630px; height: 366px;
    overflow: hidden;
    box-shadow: 0 6px 18px rgba(0,0,0,0.18);
  }
  .card--light { left: 156px; top: 112px; background: var(--card-white); }
  .card--dark {
    left: 486px; top: 548px;
    background: radial-gradient(ellipse at 55% 45%, var(--blue-bright) 0%, var(--blue-mid) 45%, var(--blue-deep) 100%);
  }
  .contact {
    position: absolute; left: 42px; top: 36px;
    font-weight: 700; font-size: 27px; line-height: 38px;
    white-space: nowrap;
  }
  .card--light .contact { color: var(--ink-blue); }
  .card--dark .contact { color: var(--ink-white); }
  .links {
    position: absolute; left: 42px; top: 178px;
    font-weight: 700; font-size: 21px; line-height: 38px;
    white-space: nowrap;
  }
  .card--light .links { color: var(--ink-blue); }
  .card--dark .links { color: var(--ink-white); }
  .links li { list-style: none; display: flex; align-items: center; gap: 10px; }
  .links svg { width: 22px; height: 22px; flex: none; }
  .vehicle {
    position: absolute; left: 78px; top: 292px;
    width: 320px; height: 70px; border-radius: 18px 18px 0 0;
  }
  .card--light .vehicle { background: linear-gradient(180deg, var(--vehicle-light), transparent); }
  .card--dark .vehicle { background: linear-gradient(180deg, var(--vehicle-dark), transparent); }
  .band {
    position: absolute; top: 0; left: 408px;
    width: 204px; height: 100%;
    display: flex; align-items: center; justify-content: center;
  }
  .card--light .band {
    background: radial-gradient(ellipse at 50% 75%, var(--blue-bright) 0%, var(--blue-mid) 45%, var(--blue-deep) 100%);
  }
  .card--dark .band {
    background: linear-gradient(90deg, #ffffff 0%, var(--card-white) 70%, var(--card-white-edge) 100%);
    box-shadow: -3px 0 8px rgba(0,0,0,0.15);
  }
  .edge { position: absolute; top: 0; right: 0; width: 18px; height: 100%; }
  .card--light .edge { background: var(--card-white-edge); }
  .card--dark .edge { background: var(--blue-deep); }
  .brand {
    writing-mode: vertical-rl; transform: rotate(180deg);
    text-align: center; font-weight: 700; line-height: 1.1;
    white-space: nowrap;
  }
  .brand__name { display: block; font-size: 39px; }
  .brand__people { display: block; font-size: 28px; font-weight: 600; }
  .card--light .brand { color: var(--ink-white); }
  .card--dark .brand__name { color: var(--ink-blue); }
  .card--dark .brand__people { color: var(--ink-cyan); }
</style>
</head>
<body>

<article class="card card--light">
  <div class="contact">
    <p>PO Box 284</p>
    <p>Brelmont WA 6172</p>
    <p>Licences: Lic 7169/2058</p>
  </div>
  <ul class="links">
    <li>
      <svg viewBox="0 0 24 24" fill="none" stroke="currentColor" stroke-width="1.8"><circle cx="12" cy="12" r="10"/><ellipse cx="12" cy="12" rx="4.5" ry="10"/><path d="M2 12h20M4 7h16M4 17h16"/></svg>
      www.VESTARPTH.com.au
    </li>
    <li>
      <svg viewBox="0 0 24 24" fill="currentColor"><path d="M6.6 2.5 9.5 6.8 7.6 9.1c1.2 2.7 3.5 5.3 6.3 6.8l2.1-1.9 4.4 2.8-1.6 3.9c-7.4.4-16-8.2-15.6-16z"/></svg>
      0427 381 592
    </li>
  </ul>
  <div class="vehicle" role="img" aria-label="Faint front view of a fleet vehicle"></div>
  <div class="band">
    <h1 class="brand"><span class="brand__name">VESTAR PTH,</span><span class="brand__people">Teodor &amp; Marguerite</span></h1>
  </div>
  <div class="edge"></div>
</article>

<article class="card card--dark">
  <div class="contact">
    <p>PO Box 284</p>
    <p>Brelmont WA 6172</p>
    <p>Licences: Lic 7169/2058</p>
  </div>
  <ul class="links">
    <li>
      <svg viewBox="0 0 24 24" fill="none" stroke="currentColor" stroke-width="1.8"><circle cx="12" cy="12" r="10"/><ellipse cx="12" cy="12" rx="4.5" ry="10"/><path d="M2 12h20M4 7h16M4 17h16"/></svg>
      www.VESTARPTH.com.au
    </li>
    <li>
      <svg viewBox="0 0 24 24" fill="currentColor"><path d="M6.6 2.5 9.5 6.8 7.6 9.1c1.2 2.7 3.5 5.3 6.3 6.8l2.1-1.9 4.4 2.8-1.6 3.9c-7.4.4-16-8.2-15.6-16z"/></svg>
      0427 381 592
    </li>
  </ul>
  <div class="vehicle" role="img" aria-label="Faint front view of a fleet vehicle"></div>
  <div class="band">
    <h2 class="brand"><span class="brand__name">VESTAR PTH,</span><span class="brand__people">Teodor &amp; Marguerite</span></h2>
  </div>
  <div class="edge"></div>
</article>

</body>
</html>
```